Halvering & Partners, LLC Business Card 2016

We need a new business card design for a very important trade show coming up.

We are a compliance Consulting Firm. Our clients are stock brokerage firms and investment advisers.

I would like our logo on both sides of the card.

Info in the front of the card shold include:

Logo
First & Last Name
Title
Office #
Cell #
Email
Company Address (42 W. Calloway Blvd., Suite 300 Pasadena, CA 91847

Back of the card should include the logo and url: www.halveringpartnersgroup.com

Target Market(s)

Stock Brokerage Firms and Investment Advisers

Industry/Entity Type

Financial Service

Contact Information for Business Card

Russell K. Halvering
President
42 W. Calloway Blvd., Suite 300
Pasadena, CA 91847
O 626.555.0147 ext. 204
C 818.555.0192
Email: russ@halveringpartnersgroup.com
www.halveringpartnersgroup.com

Requirements
Nice to have
• The back of the card could be black with the logo with the white letters.
• I do want the front of the card to at least have the color logo with the black "Halvering & Partners Lettering.

```html
<!DOCTYPE html>
<html lang="en">
<head>
<meta charset="utf-8">
<title>Halvering &amp; Partners — Business Card</title>
<link rel="stylesheet" href="https://fonts.googleapis.com/css2?family=Open+Sans:ital,wght@0,400;0,600;1,400&display=swap">
<style>
  :root {
    --backdrop: #5f4e40;
    --card-front: #ffffff;
    --card-back: #231f20;
    --accent-red: #c4262e;
    --ink-dark: #3a3a3a;
    --ink-mid: #555555;
    --ink-soft: #6f6f6f;
    --rule: #cfcfcf;
    --paper-white: #ffffff;
  }
  * { margin: 0; padding: 0; box-sizing: border-box; }
  html, body {
    width: 1200px;
    height: 987px;
    overflow: hidden;
    background: var(--backdrop);
    font-family: "Open Sans", Arial, sans-serif;
  }
  .card {
    position: absolute;
    left: 293px;
    width: 615px;
    height: 352px;
    box-shadow: 0 2px 6px rgba(0,0,0,0.35);
  }
  .card--front { top: 130px; background: var(--card-front); }
  .card--back  { top: 505px; background: var(--card-back); }

  .brand {
    position: absolute;
    left: 38px;
    top: 158px;
    display: flex;
    align-items: center;
    gap: 10px;
  }
  .brand__square {
    width: 26px;
    height: 26px;
    background: var(--accent-red);
  }
  .brand__name {
    font-size: 21px;
    font-weight: 600;
    color: var(--ink-dark);
    letter-spacing: 0.2px;
    white-space: nowrap;
  }

  .divider {
    position: absolute;
    left: 295px;
    top: 75px;
    width: 1px;
    height: 205px;
    background: var(--rule);
  }

  .contact {
    position: absolute;
    left: 317px;
    top: 74px;
  }
  .contact__name {
    font-size: 21px;
    font-weight: 600;
    color: var(--accent-red);
    line-height: 26px;
  }
  .contact__title {
    font-size: 16px;
    color: var(--ink-soft);
    line-height: 22px;
  }
  .contact__address {
    margin-top: 9px;
    font-size: 16px;
    color: var(--ink-mid);
    line-height: 23px;
  }
  .contact__lines {
    list-style: none;
    margin-top: 10px;
  }
  .contact__lines li {
    display: flex;
    align-items: center;
    gap: 8px;
    font-size: 16px;
    color: var(--ink-mid);
    line-height: 23.5px;
  }
  .contact__lines svg { width: 15px; height: 15px; flex: none; }

  .back-brand {
    position: absolute;
    right: 39px;
    top: 250px;
    text-align: right;
    color: var(--paper-white);
  }
  .back-brand__name {
    font-size: 30px;
    font-weight: 600;
    line-height: 36px;
    letter-spacing: 0.5px;
  }
  .back-brand__url {
    margin-top: 6px;
    font-size: 15px;
    font-style: italic;
    line-height: 20px;
  }
</style>
</head>
<body>
  <section class="card card--front" aria-label="Business card front">
    <div class="brand">
      <span class="brand__square" aria-hidden="true"></span>
      <span class="brand__name">Halvering &amp; Partners</span>
    </div>
    <div class="divider" aria-hidden="true"></div>
    <div class="contact">
      <p class="contact__name">Russell K. Halvering</p>
      <p class="contact__title">President</p>
      <p class="contact__address">42 W. Calloway Blvd., Suite 300<br>Pasadena, CA 91847</p>
      <ul class="contact__lines">
        <li>
          <svg viewBox="0 0 16 16" aria-hidden="true"><path fill="#c4262e" d="M3.6 1.5l2.2 2.6-1.3 1.6c.9 2 2.7 3.9 4.8 4.8l1.6-1.3 2.6 2.2-1.3 2.1C7 13.2 2.8 9 1.5 3z"/></svg>
          626.555.0147 ext. 204
        </li>
        <li>
          <svg viewBox="0 0 16 16" aria-hidden="true"><rect x="4" y="1" width="8" height="14" rx="1.5" fill="none" stroke="#c4262e" stroke-width="1.8"/><circle cx="8" cy="12.3" r="0.9" fill="#c4262e"/></svg>
          818.555.0192
        </li>
        <li>
          <svg viewBox="0 0 16 16" aria-hidden="true"><rect x="1" y="3.5" width="14" height="9" fill="#c4262e"/><path d="M1.5 4l6.5 5 6.5-5" fill="none" stroke="#fff" stroke-width="1.2"/></svg>
          russ@halveringpartnersgroup.com
        </li>
        <li>
          <svg viewBox="0 0 16 16" aria-hidden="true"><circle cx="8" cy="8" r="7" fill="#c4262e"/><path d="M1.5 8h13M8 1c-2.5 2-2.5 12 0 14M8 1c2.5 2 2.5 12 0 14" fill="none" stroke="#fff" stroke-width="0.9"/></svg>
          www.halveringpartnersgroup.com
        </li>
      </ul>
    </div>
  </section>

  <section class="card card--back" aria-label="Business card back">
    <div class="back-brand">
      <p class="back-brand__name">Halvering &amp; Partners</p>
      <p class="back-brand__url">www.halveringpartnersgroup.com</p>
    </div>
  </section>
</body>
</html>
```